Web Design Project - vR Advise

We want to modernise our web page profile. We have an existing web site that we are particularly not proud of (www.vradvise.com.au).
We have started to build a new web site using Plivex and we like the structure of it, but we need it to be professionally designed and implemented.

This current development site can be viewed here: dev.vradvise.com.au

We would like a complete design for the entire website, ready for deployment.

(We still need to finalise the content, as we have just developed new products that we hope to launch in August both on this web site and by a Vendor Forum.)
Updates

Reason: Project must be complete by this friday at the latest.

Target Market(s)

Larger companies where the robustness of their IT infrastructure is critical. Our tools and services provide for monitoring of every device

Industry/Entity Type

Build

Requirements
Must have
• Responsive design for different screen sizes.

BrightDock help desk software integrated with the website.
Currently can be viewed at support.vradvise.com.au
Brightdock only supports custom css.

Nice to have
• Customer experience testimonials in a rotating banner
Chirply and Pagebook links in the footer
We use Avenir as a company font.
Use company colours as in the logo (green and blue)

```html
<!DOCTYPE html>
<html lang="en">
<head>
<meta charset="utf-8">
<title>vR Advise</title>
<link href="https://fonts.googleapis.com/css2?family=Nunito+Sans:wght@300;400;600;700;800&display=swap" rel="stylesheet">
<style>
:root{
  --blue:#0aa2f0;
  --green:#7ea32b;
  --lime:#a4c532;
  --dark:#333333;
  --footer:#3a3a3a;
  --navy:#1e2a44;
  --ink:#2a2a2a;
  --grey-text:#8a8a8a;
  --page:#ececec;
  --white:#ffffff;
}
*{box-sizing:border-box;margin:0;padding:0}
html,body{width:856px;height:1200px;overflow:hidden}
body{position:relative;font-family:"Nunito Sans",sans-serif;color:var(--ink);
  background:linear-gradient(to bottom,var(--white) 0,var(--white) 264px,var(--page) 264px,var(--page) 1072px,var(--footer) 1072px)}
.abs{position:absolute}

.brand{left:140px;top:36px;display:flex;align-items:center;gap:8px;font-size:19px;font-weight:700;color:var(--blue)}
.brand-dot{width:18px;height:18px;border-radius:50%;background:var(--green)}
.nav{left:304px;top:40px;display:flex;font-size:11px;color:#444;letter-spacing:.2px}
.nav a{padding:2px 11px;border-left:1px solid #ddd;color:inherit;text-decoration:none}
.nav a:last-child{border-right:1px solid #ddd}

.hero-photo{left:85px;top:94px;width:686px;height:368px;
  background:linear-gradient(100deg,#e9eef2 0%,#cfe6f4 30%,#7fc4ea 45%,#5b6775 62%,#2d3440 78%,#d8dde2 100%);
  border:1px solid #ddd}

.column{left:142px;top:410px;width:572px;height:748px;background:var(--white)}

.headline{left:142px;top:410px;width:379px;height:173px}
.headline h1{position:absolute;left:12px;top:14px;font-size:27px;line-height:25px;font-weight:800;letter-spacing:-.3px}
.headline .l1{color:var(--blue)}
.headline .l2{color:var(--green)}
.headline .l3{color:var(--ink)}
.tagline{position:absolute;left:0;top:97px;width:379px;height:43px;background:var(--blue);
  color:var(--ink);font-size:11.5px;line-height:14px;padding:7px 11px;text-transform:uppercase}
.read-more{position:absolute;left:12px;top:148px;font-size:11.5px;color:var(--blue);text-transform:uppercase}

.quote{left:521px;top:410px;width:193px;height:173px;
  background:linear-gradient(160deg,var(--green) 0%,#a8c52e 60%,#bcd22a 100%);padding:10px 10px}
.quote h2{font-size:15.5px;font-weight:800;color:var(--white);margin-bottom:6px;letter-spacing:-.2px}
.field{height:20px;background:var(--white);border:1px solid #d7e3b0;margin-bottom:3.5px;font-size:8.5px;color:#9a9a9a;padding:4px 6px}
.field.msg{height:33px}
.submit{position:absolute;right:10px;bottom:10px;width:66px;height:21px;background:var(--navy);color:var(--white);
  font-size:10px;font-weight:800;letter-spacing:.6px;text-align:center;line-height:21px}

.banner{left:142px;top:583px;width:572px;height:172px;
  background:linear-gradient(90deg,#080c12 0%,#0d1826 30%,#1e4a6e 60%,#3b6f95 80%,#16314a 100%)}
.banner p{position:absolute;left:13px;top:52px;width:180px;color:var(--white);font-size:13px;line-height:16.5px;font-weight:300}

.about{left:158px;top:776px;width:335px;font-size:8.3px;line-height:10.5px;color:var(--grey-text);font-weight:300}
.about p{margin-bottom:6.5px}

.partners{left:524px;top:775px;width:172px;height:93px;background:linear-gradient(#fafafa,#efefef);
  box-shadow:0 2px 4px rgba(0,0,0,.12);text-align:center}
.partners h3{font-size:12px;font-weight:700;padding-top:6px;color:var(--ink)}
.partners .rule{width:150px;height:1px;background:#ddd;margin:5px auto 0}
.partner-name{position:absolute;left:32px;top:44px;display:flex;align-items:center;gap:5px;font-size:19px;font-weight:700;color:#222}
.partner-name i{width:13px;height:13px;background:var(--blue);display:block}
.arrow-l,.arrow-r{position:absolute;top:46px}
.arrow-l{left:8px}.arrow-r{right:8px}

.tile{top:894px;width:173px;height:137px;color:var(--white);text-align:center}
.tile svg{position:absolute;left:50%;top:14px;transform:translateX(-50%)}
.tile .sep{position:absolute;left:8px;right:8px;top:91px;height:1px;background:rgba(0,0,0,.12)}
.tile span{position:absolute;left:0;right:0;top:104px;font-size:10.5px;line-height:11.5px;font-weight:700}
.t-blue{left:157px;background:var(--blue)}
.t-green{left:341px;background:var(--green)}
.t-dark{left:524px;background:var(--dark)}

.testi-title{left:157px;top:1043px;font-size:16px;font-weight:800;color:var(--blue);letter-spacing:-.3px}
.avatar{left:189px;top:1070px;width:68px;height:68px;border-radius:50%;border:3px solid #e4e4e4;
  background:radial-gradient(circle at 50% 40%,#b98a6a,#3a2a24 75%)}
.quote-text{left:275px;top:1081px;width:400px;font-size:7.6px;line-height:10px;color:#333}
.quote-text cite{display:block;margin-top:6px;font-style:normal;color:#777}
.quote-text cite b{color:#555}
.t-prev{left:156px;top:1094px}.t-next{left:686px;top:1094px}

.footer-copy{left:143px;top:1173px;font-size:6.6px;color:#999}
.social{left:409px;top:1169px;display:flex;gap:3px}
.social i{width:16px;height:16px;border-radius:50%;background:#6b6b6b;display:block}
.legal{left:603px;top:1173px;font-size:6.6px;color:#999}
</style>
</head>
<body>

<header>
  <div class="abs brand"><span class="brand-dot"></span>vR Advise</div>
  <nav class="abs nav">
    <a href="#">HOME</a><a href="#">SERVICES</a><a href="#">SOLUTIONS</a><a href="#">PARTNERS</a><a href="#">ABOUT US</a><a href="#">CONTACT</a>
  </nav>
</header>

<div class="abs hero-photo" role="img" aria-label="Businessman drawing a rising chart among floating technology icons"></div>

<div class="abs column"></div>

<section class="abs headline">
  <h1><span class="l1">ANY DEVICE,</span><br><span class="l2">ANY PLATFORM,</span><br><span class="l3">ANYWHERE</span></h1>
  <div class="tagline">Cross domain, performance and service<br>level monitoring and management</div>
  <a class="read-more">&gt;&gt;Read more</a>
</section>

<form class="abs quote">
  <h2>REQUEST A QUOTE</h2>
  <div class="field">Name</div>
  <div class="field">Email</div>
  <div class="field">Telephone</div>
  <div class="field msg">Message</div>
  <div class="submit">SUBMIT</div>
</form>

<section class="abs banner" role="img" aria-label="Digital network of connected devices over a world map">
  <p>... delivers insight &amp; management into EVERY layer of Virtual and Physical infrastructure</p>
</section>

<section class="abs about">
  <p>We are an organisation that prides itself on attracting, employing, retaining and developing subject matter experts in the field of consulting, architecture and delivery.</p>
  <p>We employ the best to ensure that we deliver the best.</p>
  <p>Our extensive experience and expertise fuels the architecture and delivery practices, ensuring that what we propose to our customers we also deploy, manage and support.</p>
</section>

<aside class="abs partners">
  <h3>Partners</h3>
  <div class="rule"></div>
  <svg class="arrow-l" width="7" height="14"><path d="M6 1L1 7l5 6" fill="none" stroke="#555" stroke-width="1"/></svg>
  <div class="partner-name"><i></i>Voltara</div>
  <svg class="arrow-r" width="7" height="14"><path d="M1 1l5 6-5 6" fill="none" stroke="#555" stroke-width="1"/></svg>
</aside>

<div class="abs tile t-blue">
  <svg width="64" height="64" viewBox="0 0 64 64">
    <g fill="#fff">
      <circle cx="24" cy="22" r="14"/>
      <g stroke="#fff" stroke-width="7">
        <line x1="24" y1="2" x2="24" y2="42"/><line x1="4" y1="22" x2="44" y2="22"/>
        <line x1="10" y1="8" x2="38" y2="36"/><line x1="38" y1="8" x2="10" y2="36"/>
      </g>
      <circle cx="24" cy="22" r="6" fill="#0aa2f0"/>
      <circle cx="46" cy="44" r="8"/>
      <g stroke="#fff" stroke-width="4">
        <line x1="46" y1="32" x2="46" y2="56"/><line x1="34" y1="44" x2="58" y2="44"/>
        <line x1="38" y1="36" x2="54" y2="52"/><line x1="54" y1="36" x2="38" y2="52"/>
      </g>
      <circle cx="46" cy="44" r="3.5" fill="#0aa2f0"/>
    </g>
  </svg>
  <div class="sep"></div>
  <span>IT Consulting<br>Services</span>
</div>

<div class="abs tile t-green">
  <svg width="58" height="64" viewBox="0 0 58 64">
    <g fill="#fff">
      <rect x="22" y="2" width="14" height="11" rx="2"/>
      <rect x="27.5" y="13" width="3" height="14"/>
      <rect x="7" y="26" width="44" height="3"/>
      <rect x="7" y="26" width="3" height="18"/><rect x="27.5" y="26" width="3" height="18"/><rect x="48" y="26" width="3" height="18"/>
      <rect x="2" y="42" width="13" height="12" rx="2"/><rect x="22" y="42" width="14" height="12" rx="2"/><rect x="43" y="42" width="13" height="12" rx="2"/>
    </g>
  </svg>
  <div class="sep"></div>
  <span>IT Architecture<br>Services</span>
</div>

<div class="abs tile t-dark">
  <svg width="62" height="62" viewBox="0 0 62 62">
    <circle cx="31" cy="31" r="29" fill="#fff"/>
    <circle cx="31" cy="31" r="19" fill="#333"/>
    <g stroke="#333" stroke-width="5">
      <line x1="31" y1="2" x2="31" y2="12"/><line x1="31" y1="50" x2="31" y2="60"/>
      <line x1="2" y1="31" x2="12" y2="31"/><line x1="50" y1="31" x2="60" y2="31"/>
      <line x1="10" y1="10" x2="17" y2="17"/><line x1="45" y1="45" x2="52" y2="52"/>
      <line x1="52" y1="10" x2="45" y2="17"/><line x1="10" y1="52" x2="17" y2="45"/>
    </g>
    <circle cx="31" cy="31" r="15" fill="#fff"/>
    <text x="31" y="39" font-family="Nunito Sans, sans-serif" font-size="22" font-weight="800" fill="#333" text-anchor="middle">?</text>
  </svg>
  <div class="sep" style="background:rgba(255,255,255,.08)"></div>
  <span>Professional Service<br>&amp; Support</span>
</div>

<h2 class="abs testi-title">TESTIMONIALS</h2>
<svg class="abs t-prev" width="12" height="24"><path d="M11 1L1 12l10 11" fill="none" stroke="#bbb" stroke-width="1"/></svg>
<div class="abs avatar" role="img" aria-label="Portrait photo of the client giving the testimonial"></div>
<blockquote class="abs quote-text">
  Lorem ipsum dolor sit amet, consectetuer adipiscing elit, sed diam nonummy nibh euismod tincidunt ut laoreet dolore magna aliquam erat volutpat. Ut wisi enim ad minim veniam, quis nostrud exerci tation ullamcorper suscipit lobortis nisl ut aliquip ex ea commodo consequat.
  <cite>— <b>Mira Castell,</b> Chief Executive Officer</cite>
</blockquote>
<svg class="abs t-next" width="12" height="24"><path d="M1 1l10 11L1 23" fill="none" stroke="#bbb" stroke-width="1"/></svg>

<footer>
  <div class="abs footer-copy">© 2013 Copyright www.vradvise.com.au. All rights reserved.</div>
  <div class="abs social" aria-label="Pagebook and Chirply links"><i></i><i></i></div>
  <div class="abs legal">Privacy Policy &nbsp;|&nbsp; Terms &amp; Conditions</div>
</footer>

</body>
</html>
```